Hydroponic Farm Needs a Business Card

We need a business card design for a hydroponic farm located on the Gulf Coast called 'Tallowbend Farms'. We grow many forms of lettuce and tomatoes along with other herbs and spices. We currently sell to farmer's markets though will soon be expanding to commercial accounts such as restaurants and grocery stores. The colors should be bright and vibrant to reflect the nature of our produce. The final design should communicate a professional, clean, yet friendly impression and able to be used both with farmer's markets and commercial accounts.

The pictures are an example of our product. The pictures do not have to be incorporated into the business card design.

Please put areas for information such as Names, Phone Number, E-mail address, and additional information.

Industry/Entity Type

Farm

```html
<!DOCTYPE html>
<html lang="en">
<head>
<meta charset="utf-8">
<title>Tallowbend Farms – Business Card</title>
<link rel="stylesheet" href="https://fonts.googleapis.com/css2?family=Arimo:wght@400;700&display=swap">
<style>
  :root {
    --bg: #e4e5e6;
    --paper: #ffffff;
    --leaf: #5fa836;
    --leaf-light: #8cc56a;
    --leaf-deep: #3f8a26;
    --ink: #2f3a1f;
    --ink-soft: #3d3d3d;
    --lettuce-a: #9cc06a;
    --lettuce-b: #6f8f4a;
    --lettuce-c: #8a6f86;
    --vine-a: #86a862;
    --vine-b: #4f7a35;
    --soil: #6b5642;
  }
  * { box-sizing: border-box; margin: 0; padding: 0; }
  html, body { width: 1200px; height: 900px; overflow: hidden; }
  body {
    background: var(--bg);
    font-family: "Arimo", Arial, sans-serif;
    position: relative;
  }
  .card {
    position: absolute;
    left: 320px;
    width: 560px;
    height: 320px;
    overflow: hidden;
    box-shadow: 0 6px 18px rgba(0,0,0,0.18);
  }
  .card--front { top: 110px; background: var(--paper); }
  .card--back { top: 470px; background: var(--leaf); }

  .photo { position: absolute; top: 0; right: 0; bottom: 0; }
  .photo--lettuce {
    left: 300px;
    background: linear-gradient(150deg, var(--lettuce-a) 0%, var(--lettuce-b) 45%, var(--lettuce-c) 75%, var(--lettuce-a) 100%);
  }
  .photo--tomatoes {
    left: 280px;
    background: linear-gradient(180deg, var(--vine-a) 0%, var(--vine-b) 65%, var(--soil) 100%);
  }
  .shape { position: absolute; inset: 0; width: 100%; height: 100%; }

  .brand-name {
    position: absolute;
    font-weight: 700;
    line-height: 1;
    letter-spacing: -0.5px;
  }
  .card--front .brand-name { left: 40px; top: 44px; font-size: 34px; color: var(--leaf-deep); }
  .card--back .brand-name { left: 40px; top: 92px; font-size: 46px; line-height: 1.02; color: var(--paper); }

  .contact {
    position: absolute;
    left: 100px;
    top: 150px;
    font-size: 14px;
    line-height: 1.2;
    color: var(--ink-soft);
  }
  .contact__name { font-size: 19px; color: var(--ink); margin-bottom: 8px; }
  .contact__label { color: var(--leaf); }
  .contact__group { margin-bottom: 8px; }

  .price-list {
    position: absolute;
    left: 28px;
    top: 250px;
    font-size: 9.5px;
    line-height: 1.4;
    color: var(--paper);
    list-style: none;
    white-space: nowrap;
  }
</style>
</head>
<body>

<section class="card card--front" aria-label="Business card front">
  <div class="photo photo--lettuce" role="img" aria-label="Photo of green and red leaf lettuce growing"></div>
  <svg class="shape" viewBox="0 0 560 320" aria-hidden="true">
    <path d="M0 0 H392 C340 90 338 220 410 320 H0 Z" fill="var(--leaf)"/>
    <path d="M0 0 H380 C328 90 326 220 398 320 H0 Z" fill="var(--paper)"/>
  </svg>
  <div class="brand-name">Tallowbend Farms</div>
  <div class="contact">
    <p class="contact__name">Marcus Reyl</p>
    <div class="contact__group">
      <p class="contact__label">Tallowbend Farms</p>
      <p>1200 Bayou Road, Highway</p>
      <p>Gulf Coast Area</p>
    </div>
    <div class="contact__group">
      <p><span class="contact__label">Tel:</span> 555 013 2468</p>
      <p><span class="contact__label">Email:</span> marcus@tallowbendfarms.com</p>
    </div>
    <p>www.TallowbendFarms.com</p>
  </div>
</section>

<section class="card card--back" aria-label="Business card back">
  <div class="photo photo--tomatoes" role="img" aria-label="Photo of ripe tomatoes on the vine in a greenhouse"></div>
  <svg class="shape" viewBox="0 0 560 320" aria-hidden="true">
    <defs>
      <linearGradient id="panel-green" x1="0" y1="0" x2="1" y2="1">
        <stop offset="0" stop-color="var(--leaf-light)"/>
        <stop offset="1" stop-color="var(--leaf)"/>
      </linearGradient>
    </defs>
    <path d="M0 0 H362 C312 110 342 240 482 320 H0 Z" fill="var(--leaf-deep)" opacity="0.55"/>
    <path d="M0 0 H350 C300 110 330 240 470 320 H0 Z" fill="url(#panel-green)"/>
  </svg>
  <div class="brand-name">Tallowbend<br>Farms</div>
  <ul class="price-list">
    <li>Sample Text: Hothouse tomatoes Meadowrun Farms, Marlow TX 25lb case</li>
    <li>Homegrown Tomatoes Cedar Knoll Farms, Brenton 25lb case</li>
    <li>Heirloom Tomatoes Cedar Knoll Farms, Brenton 10lb case or per lb</li>
  </ul>
</section>

</body>
</html>
```